Website Comps for Famous Southern BBQ Restaurant in Alabama

We need an authentic, brand-focused redesign for a restaurant.

We need an authentic look.
The client really likes this website.
https://pelzerpit.com/

I don't want to see a bunch of crazy colors.
Avoid image sliders on the homepage. I hate those.

Please mockup the following three pages:
Homepage
Interior page (for mockup purposes, you can do an About page)
Menu page

I only need the PSD's; not the website coded.

Here is the current website: www.dunmoresmokehouse.com

https://pelzerpit.com/

Here are some additional stock photos. New photos will be shot, but these may help for your mock-up designs.
https://www.filecrate.net/sh/83kqvtrpe21zwa9/QXM71bTr4-plWnfVoe8KtYjd?dl=0
Updates

I realize we don't have a lot of high-quality photos to work with.Those will be shot.Here are some additional stock photos that may help.https://www.filecrate.net/sh/83kqvtrpe21zwa9/QXM71bTr4-plWnfVoe8KtYjd?dl=0 Added Saturday, June 10, 2017

Target Market(s)

United states

Industry/Entity Type

Restaurant

Number of Pages Required

3 page

Font styles to use
Sans Serif

Colors

Designer to choose colors to be used in the design.

Requirements
Must have
• An authentic look.
• The client really likes this website.
• https://pelzerpit.com/
• It's simple, bold, and vintage at the same time.
• That is what we want.
• Our existing website is
• dunmoresmokehouse.com
Nice to have
• Simplicity. Something that makes the food look good.
• Possibly a background.
• Logo:
• https://www.filecrate.net/s/k58tnwpl3ovza2e/dunmore-smokehouse-ridgeway.png?dl=0
• Here is a sampling of photos for your comps:
• https://www.filecrate.net/sh/61vbqzhoewpxtn4/QLT4b8JKyRmPPwf6c2ZnHUVpe?dl=0
Should not have
• Nothing too busy.
• Not too many colors.
• Keep it simple, authentic, "down home."
• No homepage image sliders.

```html
<!DOCTYPE html>
<html lang="en">
<head>
<meta charset="utf-8">
<title>About – Dunmore Smokehouse</title>
<link href="https://fonts.googleapis.com/css2?family=Fira+Sans+Condensed:wght@500;600&family=Fira+Sans:wght@400;500;600&display=swap" rel="stylesheet">
<style>
  :root {
    --cream: #f2efe2;
    --orange: #f5a11f;
    --brown: #5a1a10;
    --red: #e8393f;
    --nav-grey: #6a6864;
    --ink: #1b1b1b;
    --photo-top: #a89a84;
    --photo-bottom: #5d4f42;
  }
  * { box-sizing: border-box; margin: 0; padding: 0; }
  html, body { width: 1200px; height: 999px; overflow: hidden; }
  body {
    position: relative;
    background: var(--cream);
    font-family: "Fira Sans", Arial, sans-serif;
    color: var(--ink);
  }
  .band {
    position: absolute; left: 0; top: 112px;
    width: 1200px; height: 198px;
    background: var(--orange);
  }
  .brand-mark {
    position: absolute; left: 34px; top: 35px;
    width: 155px; height: 154px;
    background: var(--brown);
    border-radius: 3px;
    display: flex; align-items: center; justify-content: center;
    text-align: center;
    font-family: "Fira Sans Condensed", Arial, sans-serif;
    font-weight: 600; font-size: 26px; line-height: 1.1;
    color: var(--orange);
    text-transform: uppercase;
    z-index: 2;
  }
  .main-nav a {
    position: absolute; top: 52px;
    font-family: "Fira Sans Condensed", Arial, sans-serif;
    font-weight: 500; font-size: 22px;
    color: var(--nav-grey);
    text-decoration: none;
    letter-spacing: 0.2px;
  }
  .main-nav a.is-current { color: var(--red); }
  .nav-underline {
    position: absolute; left: 329px; top: 106px;
    width: 73px; height: 6px;
    background: var(--red);
  }
  .portrait {
    position: absolute; left: 164px; top: 265px;
    width: 388px; height: 444px;
    background: linear-gradient(180deg, var(--photo-top), var(--photo-bottom));
  }
  .story-title {
    position: absolute; left: 581px; top: 265px;
    font-weight: 600; font-size: 36px;
    color: #fff; letter-spacing: 0.3px;
  }
  .story-intro {
    position: absolute; left: 582px; top: 327px;
    width: 510px;
  }
  .story-intro p, .story-more p {
    font-size: 16px; line-height: 21.6px;
  }
  .story-intro p + p { margin-top: 21.6px; }
  .story-more {
    position: absolute; left: 164px; top: 746px;
    width: 935px;
  }
  .footer-brand {
    position: absolute; left: 158px; top: 955px;
    display: flex; align-items: center; gap: 14px;
  }
  .footer-brand .dot {
    width: 30px; height: 30px; background: var(--orange);
  }
  .footer-brand span {
    font-weight: 500; font-size: 34px; color: var(--red);
  }
</style>
</head>
<body>
  <header>
    <div class="brand-mark">Dunmore<br>Smokehouse</div>
    <nav class="main-nav">
      <a style="left:257px" href="#">HOME</a>
      <a style="left:336px" class="is-current" href="#">ABOUT</a>
      <a style="left:422px" href="#">LOCATIONS</a>
      <a style="left:541px" href="#">RESTAURANT MENUS</a>
      <a style="left:737px" href="#">CATERING</a>
      <a style="left:848px" href="#">NEWS</a>
      <a style="left:922px" href="#">STORE</a>
      <a style="left:1002px" href="#">CONTACT US</a>
    </nav>
    <div class="nav-underline"></div>
  </header>

  <div class="band"></div>

  <main>
    <div class="portrait" role="img" aria-label="Photo of the founder seated at a restaurant table in front of a wall of vintage signs and license plates"></div>
    <h1 class="story-title">DUNMORE’S STORY</h1>
    <div class="story-intro">
      <p>For Cal Dunmore aka DUN, growing up in North Carolina meant a whole lot of good times BS’ing and backyard barbecuing with friends. In high school, Cal Dunmore earned himself the nickname, Dozes Until Noon, for assorted reasons that may not be revealed here. Despite the moniker, Cal went on to the hospitality business by earning a degree in Restaurant and Hospitality management from Tuscaloosa State University in 1996. Following this, Cal continued his studies in the culinary school at Ashford and Reeve University in Vail, Colorado.</p>
      <p>Back home in Charlotte, North Carolina, Cal went to work as a sous chef – a great starting point – at Harlow &amp; Pine. This multi-channel retailer of gourmet and specialty foods was a great place for Cal to hone his craft. Over the next ten years and while Cal was working as a test-kitchen chef at Lean Table Magazine in Birmingham, word was spreading among his co-workers that Cal made some pretty awesome barbeque. His email list grew to more than 200 people.</p>
    </div>
    <div class="story-more">
      <p>On his days off, Cal and a friend continued to study and learn more about the fine art of Southern barbeque. He’d done this for years since back in high school. Smoking just the right cuts of beef and pork takes time, labor and finesse, and Cal was willing to put in the hours for all three. Slow roasting over North Carolina hickory wood. “We would stay up all night drinking beer and sitting beside the pit smoking meat,” he recalls. “We made it a mission to see if we could do it and how good we could make it.”</p>
    </div>
  </main>

  <footer class="footer-brand">
    <div class="dot"></div>
    <span>Dunmore Smokehouse</span>
  </footer>
</body>
</html>
```